"Tidy Nest " A Pest Control Company needs Postcard Campaign Design

Design a visually engaging postcard for " Tidy Nest ", a new pest control company. The postcard should capture attention with bold and vibrant imagery, showcasing various pests and emphasizing our comprehensive pest control services.
This will be mailed as post Card in hope to capture new leads from residents who experience pest difficulties and wants them removed

Target Market(s)

Residential Homes

Industry/Entity Type

Pest Control

Font styles to use
Serif
Sans Serif

Colors
00AB8E
00BBA5
67D7C9
C6EFE9
E9F9F6

Requirements
Must have
• Offer: " $49 Service fee ( Small letters ) with any subscription " * SEE ATTACHMENT for Core Fundamentals - Messaging Choose about 4 and the post card size "
Nice to have
• * SEE ATTACHMENT " Picture of a pest control technician (Make sure he is branded with our logo) .

```html
<!DOCTYPE html>
<html lang="en">
<head>
<meta charset="utf-8">
<title>Tidy Nest Postcard</title>
<link rel="stylesheet" href="https://fonts.googleapis.com/css2?family=Anton&family=Open+Sans:wght@400;600;700&family=Righteous&display=swap">
<style>
  :root {
    --navy: #132a4e;
    --navy-deep: #0b1c38;
    --green: #3bb54a;
    --green-bright: #4cc742;
    --white: #ffffff;
    --paper: #eeeeee;
    --ink: #111111;
    --backdrop: #000000;
    --photo-a: #8aa37b;
    --photo-b: #d9c9a8;
  }
  * { box-sizing: border-box; margin: 0; padding: 0; }
  html, body { width: 1153px; height: 1200px; overflow: hidden; background: var(--backdrop); }
  body { position: relative; font-family: "Open Sans", Arial, sans-serif; }

  .side-label {
    position: absolute;
    color: var(--white);
    font-family: "Anton", Impact, sans-serif;
    font-size: 40px;
    letter-spacing: 1px;
  }
  .side-label--front { left: 1000px; top: 245px; }
  .side-label--back { left: 1000px; top: 820px; }

  .card {
    position: absolute;
    left: 180px;
    width: 794px;
    height: 488px;
    overflow: hidden;
  }
  .card--front { top: 96px; background: var(--navy); }
  .card--back { top: 621px; background: var(--navy); height: 482px; }

  .front-swoosh { position: absolute; inset: 0; }

  .brand {
    position: absolute;
    display: flex;
    align-items: center;
    gap: 12px;
    color: var(--navy);
    font-family: "Anton", Impact, sans-serif;
    font-size: 64px;
    line-height: 1;
    white-space: nowrap;
  }
  .brand__dot { width: 26px; height: 26px; border-radius: 50%; background: var(--green); flex: none; }
  .card--front .brand { left: 28px; top: 90px; font-size: 46px; gap: 10px; }
  .card--front .brand__dot { width: 20px; height: 20px; }

  .family-photo {
    position: absolute;
    left: 25px; top: 212px;
    width: 195px; height: 230px;
    border-radius: 90px 30px 110px 30px;
    background: linear-gradient(160deg, var(--photo-a), var(--photo-b));
  }

  .offer { position: absolute; left: 230px; top: 370px; display: flex; align-items: center; gap: 8px; color: var(--white); }
  .offer__badge {
    width: 62px; height: 62px; border-radius: 50%;
    background: var(--green);
    display: flex; align-items: center; justify-content: center;
    font-family: "Anton", Impact, sans-serif; font-size: 28px;
  }
  .offer__text { font-size: 15px; line-height: 1.15; }

  .features { position: absolute; left: 420px; top: 38px; width: 350px; }
  .feature { display: flex; gap: 10px; margin-bottom: 20px; align-items: flex-start; }
  .feature__copy { flex: 1; text-align: center; }
  .feature__title { color: var(--green-bright); font-size: 11.5px; font-weight: 700; text-transform: uppercase; margin-bottom: 4px; }
  .feature__text { color: var(--white); font-size: 10.5px; line-height: 1.35; }
  .feature__thumb { width: 30px; height: 30px; background: linear-gradient(135deg, #c9c9c9, #8f8f8f); flex: none; border: 1px solid var(--white); }

  .usp { position: absolute; left: 430px; top: 270px; }
  .usp__title { color: var(--green-bright); font-size: 21px; font-weight: 600; margin-bottom: 8px; }
  .usp__list { list-style: none; }
  .usp__list li { color: var(--white); font-size: 18px; line-height: 1.35; display: flex; align-items: center; gap: 14px; padding-left: 10px; }
  .usp__list li::before { content: ""; width: 14px; height: 14px; border-radius: 50%; background: var(--green); flex: none; }

  .about-panel {
    position: absolute; left: 33px; top: 35px;
    width: 388px; height: 410px;
    background: var(--paper);
  }
  .card--back .brand { left: 50px; top: 55px; }
  .about__title {
    position: absolute; left: 20px; top: 170px;
    color: var(--green); font-family: "Righteous", Arial, sans-serif; font-size: 38px;
  }
  .about__text {
    position: absolute; left: 20px; top: 230px; width: 355px;
    color: var(--ink); font-size: 14px; line-height: 1.42; font-weight: 600;
  }

  .post-title {
    position: absolute; left: 500px; top: 55px;
    color: var(--green); font-family: "Anton", Impact, sans-serif; font-size: 40px; letter-spacing: 1px;
  }
  .address-panel {
    position: absolute; left: 421px; top: 127px;
    width: 364px; height: 340px;
    background: var(--white);
  }
  .address__label {
    position: absolute; left: 30px; top: 50px;
    color: var(--green); font-family: "Righteous", Arial, sans-serif; font-size: 22px; letter-spacing: 1px;
  }
  .address__line { position: absolute; height: 0; border-top: 2px dashed #555; }
</style>
</head>
<body>
  <div class="side-label side-label--front">FRONT</div>
  <div class="side-label side-label--back">BACLK</div>

  <section class="card card--front">
    <svg class="front-swoosh" width="794" height="488" viewBox="0 0 794 488" aria-hidden="true">
      <path d="M0 0 H300 C250 150 210 320 230 488 H0 Z" fill="#ffffff"/>
      <path d="M300 0 H330 C280 150 245 320 262 488 H230 C210 320 250 150 300 0 Z" fill="#3bb54a"/>
    </svg>
    <div class="brand"><span class="brand__dot"></span>TIDY NEST</div>
    <div class="family-photo" role="img" aria-label="Photo of a smiling family sitting outside their home"></div>
    <div class="offer">
      <div class="offer__badge">$49</div>
      <div class="offer__text">Service fee<br>with<br>any subscription</div>
    </div>

    <div class="features">
      <div class="feature">
        <div class="feature__copy">
          <p class="feature__title">Thorough, Fast Cleanup &amp; Removal</p>
          <p class="feature__text">We ensure your home is back to normal quickly<br>without the worry of Pests</p>
        </div>
        <div class="feature__thumb" role="img" aria-label="Small photo of a technician cleaning up"></div>
      </div>
      <div class="feature">
        <div class="feature__copy">
          <p class="feature__title">Ssured Elimination</p>
          <p class="feature__text">Our professional expertise guarantees all traces of<br>rodents are gone, providing lasting comfort.</p>
        </div>
        <div class="feature__thumb" role="img" aria-label="Small photo of a rodent"></div>
      </div>
      <div class="feature">
        <div class="feature__copy">
          <p class="feature__title">Guaranteed Prevention</p>
          <p class="feature__text">Our industry-leading methods and warranty ensure you<br>never have to deal with Pests again.</p>
        </div>
        <div class="feature__thumb" role="img" aria-label="Small photo of a protected home"></div>
      </div>
    </div>

    <div class="usp">
      <h2 class="usp__title">Unique Selling Points (USPs)</h2>
      <ul class="usp__list">
        <li>Bay Area Local</li>
        <li>Family-owned and operated</li>
        <li>Professional experts and credibility</li>
        <li>Eco-friendly treatments</li>
      </ul>
    </div>
  </section>

  <section class="card card--back">
    <div class="about-panel">
      <div class="brand"><span class="brand__dot"></span>TIDY NEST</div>
      <h2 class="about__title">About us :</h2>
      <p class="about__text">Tidy Nest is the bay area's top choice for pest control. Our local, family-owned business provides fast, thorough pest control service, assured elimination, and long-term prevention with advanced, eco-friendly methods. We guarantee exceptional customer satisfaction and a pest-free home.</p>
    </div>
    <h2 class="post-title">POST CARD</h2>
    <div class="address-panel">
      <div class="address__label">ADRESS</div>
      <div class="address__line" style="left:30px; top:135px; width:305px;"></div>
      <div class="address__line" style="left:30px; top:180px; width:305px;"></div>
      <div class="address__line" style="left:30px; top:225px; width:305px;"></div>
      <div class="address__line" style="left:190px; top:265px; width:145px;"></div>
    </div>
  </section>
</body>
</html>
```